SNOW PLOW DOOR HANGERS

The Door Hangers will be 3.75" wide x 8.75" long. The door hander will be hung using a rubber band. Please use entire 3.75"x8.75 for entire design

These Door hangers will advertise Snow Plowing for residential driveways.
Flyer to say:

Delvin Snow Powing

24/7 availability
Price per push
Price per season
Place in phone number: use 555-555-5555 for now.

Target Market(s)

customers seeking to have their driveways plowed.

Industry/Entity Type

Rubber

Requirements
Must have
• The Door Hangers will be 3.75" wide x 8.75" long. The door hander will be hung using a rubber band. Please use entire 3.75"x8.75 for entire design
• These Door hangers will advertise Snow Plowing for residential driveways.
• Flyer to say:
• Delvin Snow Powing
• 24/7 availability
• Price per push
• Price per season
• Place in phone number: use 555-555-5555 for now.

```html
<!DOCTYPE html>
<html lang="en">
<head>
<meta charset="UTF-8">
<title>Delvin Snow Plowing Door Hanger</title>
<link href="https://fonts.googleapis.com/css2?family=Marcellus&family=Open+Sans:wght@400;600;700&display=swap" rel="stylesheet">
<style>
  :root {
    --sky-top: #3a62c2;
    --sky-mid: #7594d6;
    --sky-haze: #aebfe6;
    --house-snow: #e9eef8;
    --house-shade: #b9c6e0;
    --snow-light: #f6f8fc;
    --snow-shade: #e3e9f4;
    --ink-navy: #1d3a63;
    --frame-blue: #3d5c9a;
    --band-dark: #0e1a2b;
    --white: #ffffff;
  }
  * { margin: 0; padding: 0; box-sizing: border-box; }
  html, body {
    width: 1200px;
    height: 2800px;
    overflow: hidden;
    background: var(--white);
  }
  .door-hanger {
    position: relative;
    width: 1200px;
    height: 2800px;
    overflow: hidden;
    font-family: "Open Sans", Arial, sans-serif;
  }
  .house-photo {
    position: absolute;
    left: 0; top: 0;
    width: 1200px;
    height: 1150px;
    background:
      radial-gradient(ellipse 520px 260px at 640px 960px, var(--house-snow) 0%, rgba(233,238,248,0.85) 45%, rgba(233,238,248,0) 100%),
      radial-gradient(ellipse 200px 520px at 150px 820px, rgba(240,244,251,0.9) 0%, rgba(240,244,251,0) 100%),
      radial-gradient(ellipse 180px 420px at 1120px 760px, rgba(240,244,251,0.8) 0%, rgba(240,244,251,0) 100%),
      linear-gradient(180deg,
        var(--sky-top) 0%,
        var(--sky-mid) 35%,
        var(--sky-haze) 60%,
        var(--house-shade) 80%,
        var(--house-snow) 100%);
  }
  .snow-field {
    position: absolute;
    left: 0; top: 1110px;
    width: 1200px;
    height: 1258px;
    background: linear-gradient(180deg,
      var(--snow-light) 0%,
      var(--snow-shade) 35%,
      var(--snow-light) 70%,
      var(--snow-shade) 100%);
  }
  .brand {
    position: absolute;
    left: 0; top: 140px;
    width: 100%;
    text-align: center;
    color: var(--white);
  }
  .brand-name {
    font-family: "Marcellus", Georgia, serif;
    font-size: 168px;
    font-weight: 400;
    letter-spacing: 8px;
    line-height: 1;
  }
  .brand-service {
    margin-top: 44px;
    font-size: 60px;
    font-weight: 400;
    letter-spacing: 24px;
    padding-left: 24px;
    line-height: 1;
  }
  .offer-frame {
    position: absolute;
    left: 148px; top: 1292px;
    width: 900px;
    height: 852px;
    border: 6px dashed var(--frame-blue);
    display: flex;
    flex-direction: column;
    align-items: center;
    justify-content: center;
    gap: 50px;
    color: var(--ink-navy);
    text-align: center;
    padding-top: 20px;
  }
  .offer-line {
    font-size: 92px;
    font-weight: 600;
    line-height: 1.1;
  }
  .offer-line .highlight {
    font-size: 118px;
    font-weight: 700;
  }
  .contact-band {
    position: absolute;
    left: 0; top: 2368px;
    width: 1200px;
    height: 432px;
    background: var(--band-dark);
    display: flex;
    align-items: center;
    justify-content: center;
  }
  .phone-number {
    color: var(--white);
    font-size: 122px;
    font-weight: 400;
    letter-spacing: 1px;
  }
</style>
</head>
<body>
  <main class="door-hanger">
    <div class="house-photo" role="img" aria-label="Photo of a snow-covered house and snow-laden fir trees under a blue winter sky"></div>
    <div class="snow-field" role="img" aria-label="Close-up photo of a field of fresh deep snow"></div>

    <header class="brand">
      <h1 class="brand-name">DELVIN</h1>
      <p class="brand-service">SNOW PLOWING</p>
    </header>

    <section class="offer-frame">
      <p class="offer-line"><span class="highlight">24/7</span> availability</p>
      <p class="offer-line">Price per push</p>
      <p class="offer-line">Price per season</p>
    </section>

    <footer class="contact-band">
      <p class="phone-number">555-555-5555</p>
    </footer>
  </main>
</body>
</html>
```